Healthcare food company need product packaging design

We need a food supplements product packaging design for an all natural wholesome food.
For natural wholesome design, we need a fresh and clean looking label as the products contain soybean, kale and broccoli as an alternative protein food powder. To appeal to the health conscious consumer .

Target Market(s)

For natural wholesome food, all age group

Industry/Entity Type

Health And Wellness

Font styles to use
Serif
Sans Serif

Requirements
Must have
• Strong colours and bigger font size to attract consumer when product is placed on shelf
Nice to have
• Fresh vegetable colours with elements of green or mutiple colours
Should not have
• No restriction

```html
<!DOCTYPE html>
<html lang="en">
<head>
<meta charset="utf-8">
<title>VerdeBase Protien Powder – Label Variants</title>
<link href="https://fonts.googleapis.com/css2?family=Open+Sans:wdth,wght@75..100,300..800&family=Arimo:wght@400;700&family=Tinos&display=swap" rel="stylesheet">
<style>
  :root{
    --board:#9c9c9c;
    --forest:#0e5a31;
    --moss:#4b7c34;
    --olive:#3e6a2a;
    --charcoal:#4a4a4a;
    --ink:#111;
    --paper:#fff;
  }
  html,body{margin:0;padding:0;width:1200px;height:1200px;overflow:hidden;background:var(--board);}
  .board{position:relative;width:1200px;height:1200px;}
  .label{
    position:absolute;left:218px;width:955px;height:468px;
    transform:scale(.8);transform-origin:0 0;
    background:var(--label-bg);overflow:hidden;
    font-family:"Open Sans",sans-serif;
  }
  .label--white{top:14px;
    --label-bg:var(--paper);--band:var(--charcoal);--band-text:var(--paper);
    --all:var(--ink);--plant:var(--forest);--source:var(--charcoal);--protien:var(--forest);
    --powder:var(--ink);--feature:var(--ink);--num:var(--olive);--unit:var(--charcoal);
    --contain-head:var(--olive);--contain-list:var(--ink);--seal:var(--forest);}
  .label--forest{top:408px;
    --label-bg:var(--forest);--band:var(--paper);--band-text:var(--forest);
    --all:var(--ink);--plant:#2f6a2c;--source:var(--paper);--protien:var(--paper);
    --powder:var(--ink);--feature:var(--paper);--num:#3c6b2a;--unit:var(--paper);
    --contain-head:#3c6b2a;--contain-list:var(--paper);--seal:var(--forest);}
  .label--moss{top:802px;
    --label-bg:var(--moss);--band:var(--forest);--band-text:var(--paper);
    --all:var(--ink);--plant:var(--paper);--source:var(--ink);--protien:var(--forest);
    --powder:var(--ink);--feature:var(--paper);--num:var(--paper);--unit:var(--ink);
    --contain-head:var(--ink);--contain-list:var(--ink);--seal:var(--forest);}

  .band{position:absolute;left:0;top:0;width:955px;height:120px;}
  .band path{fill:var(--band);}
  .band-title{position:absolute;left:205px;top:52px;font-family:"Tinos",serif;font-size:23px;letter-spacing:3.2px;color:var(--band-text);}

  .brand-seal{position:absolute;left:35px;top:22px;width:98px;height:98px;border-radius:50%;
    background:var(--seal);border:4px solid var(--paper);box-shadow:0 0 0 2px var(--seal);
    display:flex;align-items:center;justify-content:center;
    color:var(--paper);font-family:"Open Sans",sans-serif;font-weight:700;font-size:14px;letter-spacing:1px;text-align:center;line-height:1.1;}

  .basket{position:absolute;left:0;top:188px;width:238px;height:280px;
    border-radius:0 75% 0 0 / 0 45% 0 0;
    background:radial-gradient(circle at 45% 40%,#e9a63a 0%,#c9602a 30%,#8f9b2e 55%,#9a6a2f 80%,#7a4f22 100%);}

  .vert{position:absolute;transform:rotate(-90deg);transform-origin:0 0;white-space:nowrap;}
  .all-tag{left:93px;top:188px;font-weight:700;font-size:24px;color:var(--all);}
  .powder-tag{left:484px;top:266px;font-size:16px;letter-spacing:.5px;color:var(--powder);}

  .product-name{position:absolute;left:118px;top:122px;margin:0;font-weight:700;font-size:62px;font-stretch:90%;letter-spacing:-1px;line-height:1;}
  .product-name .p1{color:var(--plant);}
  .product-name .p2{color:var(--source);}
  .product-type{position:absolute;left:92px;top:182px;margin:0;font-weight:700;font-size:94px;font-stretch:82%;letter-spacing:-1px;line-height:1;color:var(--protien);}

  .features{position:absolute;right:462px;top:280px;margin:0;padding:0;list-style:none;text-align:right;
    font-size:21px;line-height:28px;color:var(--feature);}
  .weight{position:absolute;right:462px;top:404px;font-weight:700;font-size:38px;line-height:1;}
  .weight .n{color:var(--num);}
  .weight .u{color:var(--unit);}

  .facts{position:absolute;left:585px;top:118px;width:266px;background:var(--paper);
    border:1px solid #555;padding:3px 6px 4px;font-family:"Arimo",sans-serif;color:var(--ink);}
  .facts h2{margin:0;font-size:26px;line-height:28px;font-weight:700;}
  .facts .serving{font-size:11px;line-height:13px;}
  .facts .bar{height:6px;background:var(--ink);margin:2px 0;}
  .facts table{width:100%;border-collapse:collapse;font-size:11.5px;}
  .facts th{font-size:8.5px;line-height:9px;font-weight:700;text-align:center;padding:2px 0 3px;border-bottom:4px solid var(--ink);}
  .facts td{padding:2px 0;line-height:14px;border-bottom:1px solid #999;}
  .facts td:nth-child(2){width:70px;}
  .facts td:nth-child(3){width:46px;text-align:right;padding-right:6px;}
  .facts td.indent{padding-left:14px;}
  .facts tr.thick td{border-bottom:7px solid var(--ink);}
  .facts .note{font-size:8px;line-height:15px;margin-top:2px;}

  .contains{left:883px;top:440px;font-size:15px;line-height:20px;}
  .contains b{color:var(--contain-head);font-weight:700;}
  .contains span{color:var(--contain-list);}
</style>
</head>
<body>
<main class="board">

  <section class="label label--white">
    <svg class="band" viewBox="0 0 955 120" aria-hidden="true"><path d="M0,66 Q480,30 955,45 L955,78 Q480,82 0,102 Z"/></svg>
    <div class="band-title">Nutritional Supplement</div>
    <div class="brand-seal">LUMI<br>LEAF</div>
    <div class="basket" role="img" aria-label="Wicker basket filled with fresh fruit"></div>
    <div class="vert all-tag">ALL</div>
    <h1 class="product-name"><span class="p1">Verde</span><span class="p2">Base</span></h1>
    <p class="product-type">PROTIEN</p>
    <div class="vert powder-tag">POWDER</div>
    <ul class="features"><li>High protein Content</li><li>Added DHA</li><li>Essential Vitamins</li><li>Essential Minerals</li></ul>
    <div class="weight"><span class="n">300</span><span class="u">g</span></div>
    <div class="facts">
      <h2>Supplement Facts</h2>
      <div class="serving">Serving Size 1 scoop (22g)<br>Servings Per Container about 41</div>
      <div class="bar"></div>
      <table>
        <tr><th></th><th>Amount Per<br>Serving</th><th>% Daily<br>Value</th></tr>
        <tr><td>Calories</td><td>80</td><td></td></tr>
        <tr><td class="indent">Calories from Fat</td><td>0</td><td></td></tr>
        <tr><td>Total Fat</td><td>0 g</td><td>0%*</td></tr>
        <tr><td>Total Carbohydrate</td><td>0 g</td><td>0%*</td></tr>
        <tr><td class="indent">Sugars</td><td>0 g</td><td>**</td></tr>
        <tr><td>Protein</td><td>20 g</td><td>40%*</td></tr>
        <tr><td>Calcium</td><td>10 mg</td><td>1%</td></tr>
        <tr class="thick"><td>Sodium</td><td>170 mg</td><td>7%</td></tr>
        <tr class="thick"><td>Leucine</td><td>2.5 g</td><td>**</td></tr>
      </table>
      <div class="note">*Percent Daily Values are based on a 2,000 calorie diet.<br>**Daily Value not established.</div>
    </div>
    <div class="vert contains"><b>CONTAIN:</b><br><span>Kale,Soy Bean Powder, Pea Powder, Lecithin</span></div>
  </section>

  <section class="label label--forest">
    <svg class="band" viewBox="0 0 955 120" aria-hidden="true"><path d="M0,66 Q480,30 955,45 L955,78 Q480,82 0,102 Z"/></svg>
    <div class="band-title">Nutritional Supplement</div>
    <div class="brand-seal">LUMI<br>LEAF</div>
    <div class="basket" role="img" aria-label="Wicker basket filled with fresh fruit"></div>
    <div class="vert all-tag">ALL</div>
    <h1 class="product-name"><span class="p1">Verde</span><span class="p2">Base</span></h1>
    <p class="product-type">PROTIEN</p>
    <div class="vert powder-tag">POWDER</div>
    <ul class="features"><li>High protein Content</li><li>Added DHA</li><li>Essential Vitamins</li><li>Essential Minerals</li></ul>
    <div class="weight"><span class="n">300</span><span class="u">g</span></div>
    <div class="facts">
      <h2>Supplement Facts</h2>
      <div class="serving">Serving Size 1 scoop (22g)<br>Servings Per Container about 41</div>
      <div class="bar"></div>
      <table>
        <tr><th></th><th>Amount Per<br>Serving</th><th>% Daily<br>Value</th></tr>
        <tr><td>Calories</td><td>80</td><td></td></tr>
        <tr><td class="indent">Calories from Fat</td><td>0</td><td></td></tr>
        <tr><td>Total Fat</td><td>0 g</td><td>0%*</td></tr>
        <tr><td>Total Carbohydrate</td><td>0 g</td><td>0%*</td></tr>
        <tr><td class="indent">Sugars</td><td>0 g</td><td>**</td></tr>
        <tr><td>Protein</td><td>20 g</td><td>40%*</td></tr>
        <tr><td>Calcium</td><td>10 mg</td><td>1%</td></tr>
        <tr class="thick"><td>Sodium</td><td>170 mg</td><td>7%</td></tr>
        <tr class="thick"><td>Leucine</td><td>2.5 g</td><td>**</td></tr>
      </table>
      <div class="note">*Percent Daily Values are based on a 2,000 calorie diet.<br>**Daily Value not established.</div>
    </div>
    <div class="vert contains"><b>CONTAIN:</b><br><span>Kale,Soy Bean Powder, Pea Powder, Lecithin</span></div>
  </section>

  <section class="label label--moss">
    <svg class="band" viewBox="0 0 955 120" aria-hidden="true"><path d="M0,66 Q480,30 955,45 L955,78 Q480,82 0,102 Z"/></svg>
    <div class="band-title">Nutritional Supplement</div>
    <div class="brand-seal">LUMI<br>LEAF</div>
    <div class="basket" role="img" aria-label="Wicker basket filled with fresh fruit"></div>
    <div class="vert all-tag">ALL</div>
    <h1 class="product-name"><span class="p1">Verde</span><span class="p2">Base</span></h1>
    <p class="product-type">PROTIEN</p>
    <div class="vert powder-tag">POWDER</div>
    <ul class="features"><li>High protein Content</li><li>Added DHA</li><li>Essential Vitamins</li><li>Essential Minerals</li></ul>
    <div class="weight"><span class="n">300</span><span class="u">g</span></div>
    <div class="facts">
      <h2>Supplement Facts</h2>
      <div class="serving">Serving Size 1 scoop (22g)<br>Servings Per Container about 41</div>
      <div class="bar"></div>
      <table>
        <tr><th></th><th>Amount Per<br>Serving</th><th>% Daily<br>Value</th></tr>
        <tr><td>Calories</td><td>80</td><td></td></tr>
        <tr><td class="indent">Calories from Fat</td><td>0</td><td></td></tr>
        <tr><td>Total Fat</td><td>0 g</td><td>0%*</td></tr>
        <tr><td>Total Carbohydrate</td><td>0 g</td><td>0%*</td></tr>
        <tr><td class="indent">Sugars</td><td>0 g</td><td>**</td></tr>
        <tr><td>Protein</td><td>20 g</td><td>40%*</td></tr>
        <tr><td>Calcium</td><td>10 mg</td><td>1%</td></tr>
        <tr class="thick"><td>Sodium</td><td>170 mg</td><td>7%</td></tr>
        <tr class="thick"><td>Leucine</td><td>2.5 g</td><td>**</td></tr>
      </table>
      <div class="note">*Percent Daily Values are based on a 2,000 calorie diet.<br>**Daily Value not established.</div>
    </div>
    <div class="vert contains"><b>CONTAIN:</b><br><span>Kale,Soy Bean Powder, Pea Powder, Lecithin</span></div>
  </section>

</main>
</body>
</html>
```